Harborline Cremations Business Cards

To create a business card for my company Harborline Cremations. Remember it is a cremation company.
We want to make sure people have a business card and information. Something modern, professional
100% Online
Prices starting at $695 all-inclusive (prices subject to change without notice).
A business card is the first point of contact with the prospective client.

Contact Information for Business Card

(305) 418-7260
www.HarborlineCremationsMiami.example
harborlinecremations@mailbox.example

Requirements
Must have
• 100% Online
Prices starting at $695 all-inclusive (prices subject to change without notice)

(305) 418-7260

Must match logo style
Should not have
• No black backgrounds. Please only use the white, orange and blue from the logo

```html
<!DOCTYPE html>
<html lang="en">
<head>
<meta charset="utf-8">
<title>Harborline Cremations – Business Cards</title>
<link rel="stylesheet" href="https://fonts.googleapis.com/css2?family=Lato:wght@400;700&family=Raleway:wght@700&display=swap">
<style>
  :root {
    --blue: #03a0e6;
    --orange: #fe8708;
    --orange-dark: #d96400;
    --white: #ffffff;
    --page: #ffffff;
    --hatch: #efefef;
  }
  * { margin: 0; padding: 0; box-sizing: border-box; }
  html, body { width: 1200px; height: 1200px; overflow: hidden; background: var(--page); }
  .canvas { position: relative; width: 1200px; height: 1200px; font-family: "Lato", sans-serif; }
  .card {
    position: absolute; left: 262px; width: 676px; height: 406px;
    background: var(--white); overflow: hidden;
    box-shadow: 0 6px 22px rgba(0,0,0,0.18);
  }
  .card--front { top: 160px; }
  .card--back { top: 635px; }
  .card svg.card__art { position: absolute; inset: 0; }
  .wordmark {
    position: absolute; text-align: center; color: var(--blue);
    font-family: "Lato", sans-serif; font-weight: 700; letter-spacing: 0.06em; line-height: 1.05;
  }
  .wordmark__dot { position: absolute; border-radius: 50%; background: var(--orange); }
  .front__logo { left: 16px; top: 190px; width: 300px; font-size: 30px; }
  .front__dot { left: 121px; top: 86px; width: 90px; height: 90px; }
  .front__title {
    position: absolute; left: 366px; top: 66px; color: var(--white);
    font-family: "Raleway", sans-serif; font-weight: 700; font-size: 26px;
  }
  .front__subtitle { position: absolute; left: 366px; top: 104px; color: var(--white); font-size: 20px; }
  .front__phone { position: absolute; left: 382px; top: 191px; color: var(--white); font-size: 22px; }
  .front__online {
    position: absolute; left: 554px; top: 150px; width: 68px; text-align: center;
    color: var(--white); font-weight: 700; font-size: 16px; line-height: 1.3;
  }
  .front__contact { position: absolute; left: 356px; top: 280px; color: var(--white); font-size: 16px; line-height: 1.4; }
  .back__logo { left: 88px; top: 180px; width: 500px; font-size: 40px; }
  .back__dot { left: 278px; top: 50px; width: 120px; height: 120px; }
  .back__price {
    position: absolute; left: 0; width: 676px; top: 306px; text-align: center;
    color: var(--white); font-size: 22px;
  }
  .back__note {
    position: absolute; left: 0; width: 676px; top: 335px; text-align: center;
    color: var(--white); font-size: 13px;
  }
</style>
</head>
<body>
<main class="canvas">

  <section class="card card--front" aria-label="Business card front">
    <svg class="card__art" viewBox="0 0 676 406" width="676" height="406" aria-hidden="true">
      <defs>
        <clipPath id="edge-accents"><rect x="0" y="0" width="676" height="54"/><rect x="0" y="355" width="676" height="51"/></clipPath>
      </defs>
      <path d="M320 0 L676 0 L676 406 L332 406 Q282 200 320 0 Z" fill="var(--orange)" clip-path="url(#edge-accents)"/>
      <path d="M334 0 L676 0 L676 406 L346 406 Q296 200 334 0 Z" fill="var(--blue)"/>
      <rect x="302" y="148" width="22" height="104" rx="10" fill="var(--orange-dark)"/>
      <path d="M302 166 L676 168 L676 236 L302 238 Z" fill="var(--orange)"/>
      <circle cx="588" cy="176" r="34" fill="var(--blue)"/>
      <circle cx="354" cy="205" r="22" fill="var(--white)"/>
      <path d="M346 193 q4 -3 6 0 l3 6 q1 3 -2 4 l-2 1 q2 6 7 10 l2 -2 q2 -2 4 0 l5 4 q2 3 -1 5 l-3 2 q-6 2 -14 -8 q-8 -10 -6 -18 z" fill="var(--orange)"/>
      <circle cx="333" cy="302" r="16" fill="var(--orange)"/>
      <rect x="327" y="292" width="12" height="19" rx="6" fill="var(--white)"/>
      <line x1="333" y1="293" x2="333" y2="300" stroke="var(--orange)" stroke-width="2"/>
      <line x1="327" y1="300" x2="339" y2="300" stroke="var(--orange)" stroke-width="2"/>
    </svg>
    <span class="wordmark__dot front__dot"></span>
    <p class="wordmark front__logo">HARBORLINE<br>CREMATIONS</p>
    <h1 class="front__title">Harborline Cremations</h1>
    <p class="front__subtitle">company</p>
    <p class="front__phone">(305) 418-7260</p>
    <p class="front__online">100%<br>Online</p>
    <p class="front__contact">www.HarborlineCremationsMiami.example<br>harborlinecremations@mailbox.example</p>
  </section>

  <section class="card card--back" aria-label="Business card back">
    <svg class="card__art" viewBox="0 0 676 406" width="676" height="406" aria-hidden="true">
      <defs>
        <clipPath id="side-accents"><rect x="0" y="250" width="86" height="100"/><rect x="591" y="250" width="85" height="100"/></clipPath>
      </defs>
      <path d="M0 313 Q338 240 676 313 L676 333 Q338 260 0 333 Z" fill="var(--hatch)"/>
      <path d="M0 313 Q338 240 676 313 L676 333 Q338 260 0 333 Z" fill="var(--orange)" clip-path="url(#side-accents)"/>
      <rect x="252" y="275" width="172" height="30" fill="var(--orange)"/>
      <path d="M0 333 Q338 260 676 333 L676 406 L0 406 Z" fill="var(--blue)"/>
    </svg>
    <span class="wordmark__dot back__dot"></span>
    <p class="wordmark back__logo">HARBORLINE<br>CREMATIONS</p>
    <p class="back__price">Prices starting at $695 all-inclusive</p>
    <p class="back__note">(prices subject to change without notice)</p>
  </section>

</main>
</body>
</html>
```